College Admissions Consulting needs a small street facing sign for new office location.

I need a graphic design to be used inside window for a banner/sign in office location on a high walking traffic city street, for my company, Campus Lantern. I work with high school students and families on the college planning and selection application process. Please check out the website to learn more about what I do (www.mycampuslantern.example). The banner will be used to market our services at our office location. The final design should utilize logo colors, phone number, and website/email information. I'd like to incorporate a my picture in someway because of face recognition. To be printed on a posterboard or vinyl banner.

Target Market(s)

Parents of high school aged children.

Industry/Entity Type

Education

Font styles to use
Sans Serif

Colors
abd037

Requirements
Must have
• Clean, attractive, and professional design. Attract the attention of people walking by. Information must be clear and readable (phone/email, etc.).
Nice to have
• Utilize the picture with crossed arms (without the brown background on picture).
Emphasize tagline:
Mastering The College Admission Process
....with personalized, professional guidance in planning, selecting, and applying to the right colleges.

```html
<!DOCTYPE html>
<html lang="en">
<head>
<meta charset="utf-8">
<title>Campus Lantern – Window Banner</title>
<link rel="stylesheet" href="https://fonts.googleapis.com/css2?family=Arimo:wght@400;700&display=swap">
<style>
  :root {
    --page: #ffffff;
    --charcoal: #333132;
    --green-light: #acd57b;
    --green-mid: #8bc34a;
    --green-deep: #6aab4c;
    --green-brand: #7cc142;
    --footer-light: #a3d474;
    --navy: #004a8f;
    --ink: #2f2f2f;
    --white: #ffffff;
  }
  * { margin: 0; padding: 0; box-sizing: border-box; }
  html, body {
    width: 687px; height: 1200px; overflow: hidden;
    background: var(--page);
    font-family: "Arimo", Arial, sans-serif;
  }
  .banner {
    position: absolute; left: 43px; top: 0;
    width: 600px; height: 1200px; overflow: hidden;
    background: var(--green-mid);
  }
  .banner-shapes { position: absolute; inset: 0; }
  .brand {
    position: absolute; left: 26px; top: 40px;
    display: flex; align-items: center; gap: 14px;
  }
  .brand-dot {
    width: 50px; height: 50px; border-radius: 50%;
    background: var(--green-brand);
  }
  .brand-name {
    font-size: 33px; font-weight: 400; color: var(--white);
    white-space: nowrap;
  }
  .brand-tagline {
    position: absolute; left: 94px; top: 86px;
    font-size: 9.5px; font-weight: 700; color: var(--white);
    letter-spacing: 0.5px; text-transform: uppercase; white-space: nowrap;
  }
  .consultant-photo {
    position: absolute; left: 359px; top: 0;
    width: 209px; height: 294px;
    border: 4px solid var(--white); border-top: 0;
    border-radius: 0 0 22px 22px;
    background: linear-gradient(160deg, #9c8a6c 0%, #7a6650 55%, #2a2624 100%);
  }
  .benefit { position: absolute; color: var(--ink); }
  .benefit h2 {
    font-size: 35px; font-weight: 700; color: var(--navy);
    line-height: 38.5px; white-space: nowrap;
  }
  .benefit p { font-size: 25px; line-height: 29px; white-space: nowrap; }
  .benefit--personal { left: 68px; top: 331px; }
  .benefit--empowered { left: 119px; top: 466px; }
  .benefit--choice { left: 172px; top: 604px; }
  .students-photo {
    position: absolute; left: 236px; top: 729px;
    width: 354px; height: 252px;
    border-radius: 150px 150px 0 0;
    background: linear-gradient(180deg, #c9a48a 0%, #e9e4dd 45%, #2f8a3e 100%);
  }
  .contact { position: absolute; left: 58px; top: 1021px; color: var(--ink); }
  .contact h3 { font-size: 20.5px; font-weight: 700; margin-bottom: 10px; color: #333; }
  .contact-row {
    display: flex; align-items: center; gap: 6px;
    font-size: 17px; height: 36px; white-space: nowrap;
  }
  .contact-row svg { width: 17px; height: 17px; flex: none; }
  .contact-at { width: 17px; font-size: 19px; }
</style>
</head>
<body>
<main class="banner">
  <svg class="banner-shapes" viewBox="0 0 600 1200" width="600" height="1200" aria-hidden="true">
    <defs>
      <radialGradient id="glow" cx="50" cy="190" r="170" gradientUnits="userSpaceOnUse">
        <stop offset="0" stop-color="#6db64a"/>
        <stop offset="1" stop-color="#acd57b" stop-opacity="0"/>
      </radialGradient>
    </defs>
    <polygon points="0,0 600,0 600,759 136,906 0,294" fill="var(--green-light)"/>
    <polygon points="0,0 600,0 600,759 136,906 0,294" fill="url(#glow)"/>
    <polygon points="0,294 136,906 600,759 600,776 121,941 0,310" fill="var(--green-deep)"/>
    <polygon points="0,0 600,0 600,216 0,126" fill="var(--charcoal)"/>
    <polyline points="53,345 53,452 107,452 107,581 159,581 159,707"
      fill="none" stroke="#6aab4c" stroke-width="2" stroke-dasharray="2 3"/>
    <circle cx="53" cy="345" r="3.5" fill="#6aab4c"/>
    <circle cx="159" cy="707" r="3.5" fill="#6aab4c"/>
    <rect x="0" y="981" width="600" height="15" fill="var(--green-deep)"/>
    <rect x="0" y="996" width="600" height="204" fill="var(--green-mid)"/>
    <path d="M0,996 L386,996 C420,1050 420,1150 370,1200 L0,1200 Z" fill="var(--footer-light)"/>
  </svg>

  <header class="brand-block">
    <div class="brand">
      <span class="brand-dot"></span>
      <span class="brand-name">Campus Lantern</span>
    </div>
    <div class="brand-tagline">Mastering the College Admission Process</div>
  </header>

  <div class="consultant-photo" role="img" aria-label="Portrait of the consultant with arms crossed"></div>

  <section class="benefit benefit--personal">
    <h2>Get Personal</h2>
    <p>A Highly Individualized Approach backed<br>by 20 Years of Experience</p>
  </section>
  <section class="benefit benefit--empowered">
    <h2>Get Empowered</h2>
    <p>Work With an Expert to Take Control<br>of Your Campus Lantern Plan</p>
  </section>
  <section class="benefit benefit--choice">
    <h2>Which “U” Is for you?</h2>
    <p>Expert Help to Focus the College<br>Search and Strengthen Applications</p>
  </section>

  <div class="students-photo" role="img" aria-label="Two smiling high school students, one pointing, one holding folders"></div>

  <footer class="contact">
    <h3>CONTACT INFORMATION</h3>
    <div class="contact-row">
      <svg viewBox="0 0 24 24"><path d="M6.6 2.5l3 4-2 2.5c1.3 2.8 3.4 4.9 6.2 6.2l2.5-2 4 3-1.8 3.3C11 19.5 4.5 13 3.5 4.3z" fill="#2f2f2f"/></svg>
      <span>: 555-014-PLAN (7526)</span>
    </div>
    <div class="contact-row">
      <span class="contact-at">@</span>
      <span>: hello@mycampuslantern.example</span>
    </div>
    <div class="contact-row">
      <svg viewBox="0 0 24 24" fill="none" stroke="#2f2f2f" stroke-width="2"><circle cx="12" cy="12" r="10"/><ellipse cx="12" cy="12" rx="4.5" ry="10"/><line x1="2" y1="12" x2="22" y2="12"/><line x1="4" y1="6.5" x2="20" y2="6.5"/><line x1="4" y1="17.5" x2="20" y2="17.5"/></svg>
      <span>: http://www.mycampuslantern.example</span>
    </div>
  </footer>
</main>
</body>
</html>
```